Postcard to market investment strategy

Harborline Capital Partners (HCP) has offered investment solutions for over 30 years and we would like to highlight one of our Separately Managed Accounts (SMA) strategies. The strategy is called “Steady Harvest” and is an income focused strategy with a track record exceeding 5 years. The strategy invests in a basket of Closed End Funds that are currently selling at attractive discounts, pay a high dividend and based on our outlook offer net asset value appreciation potential. This strategy has a strong track record and key points to consider include:
1. Top Ranked Strategy
2. Above Average Income
3. Available in both SMA and UMA
4. Minimums as low as $50,000
5. Current Income around 6% to 7%
6. Outpaced the Q&R 700 since inception

Industry/Entity Type

Investment

```html
<!DOCTYPE html>
<html lang="en">
<head>
<meta charset="utf-8">
<title>Steady Harvest – Harborline Capital Partners</title>
<link href="https://fonts.googleapis.com/css2?family=Quicksand:wght@600;700&family=Lato:wght@400;700&display=swap" rel="stylesheet">
<style>
  :root {
    --backdrop: #6e6e6e;
    --card-light: #ffffff;
    --card-shade: #e4e4e4;
    --brand-blue: #1d4f91;
    --figure-blue: #0d4f9e;
    --accent-orange: #f7941d;
    --ribbon-blue: #0fa3e0;
    --ribbon-pink: #e6007e;
    --ribbon-wine: #a3344a;
    --ribbon-lime: #b7cf0f;
    --ribbon-teal: #3ccfbb;
    --ribbon-grey: #6d6d6d;
    --icon-white: #ffffff;
  }
  * { margin: 0; padding: 0; box-sizing: border-box; }
  html, body { width: 1200px; height: 822px; overflow: hidden; background: var(--backdrop); }
  .canvas { position: relative; width: 1200px; height: 822px; }
  .postcard {
    position: absolute; left: 60px; top: 30px; width: 1068px; height: 757px;
    background: linear-gradient(120deg, var(--card-light) 35%, var(--card-shade) 100%);
    overflow: hidden;
  }
  .network-backdrop {
    position: absolute; inset: 0;
    background: radial-gradient(ellipse at 85% 40%, rgba(150,150,150,0.18), transparent 60%),
                radial-gradient(ellipse at 20% 95%, rgba(150,150,150,0.15), transparent 55%);
  }
  .brand { position: absolute; left: 208px; top: 155px; color: var(--brand-blue); font-family: "Lato", sans-serif; font-weight: 400; }
  .brand-mark { position: absolute; left: 0; top: 0; width: 42px; height: 42px; background: var(--brand-blue); }
  .brand-initials { position: absolute; left: 58px; top: -6px; font-size: 50px; letter-spacing: 14px; line-height: 1; }
  .brand-name { position: absolute; left: 0; top: 60px; font-size: 14.5px; letter-spacing: 1.4px; white-space: nowrap; text-transform: uppercase; }
  .advisor-figure {
    position: absolute; left: 470px; top: 45px; width: 160px; height: 205px;
    background: linear-gradient(180deg, var(--figure-blue), #0a3f80);
    border-radius: 60px 60px 10px 10px;
  }
  .title {
    position: absolute; left: 652px; top: 142px; color: var(--accent-orange);
    font-family: "Quicksand", sans-serif; font-weight: 700; line-height: 1;
  }
  .title-line { display: block; font-size: 41px; letter-spacing: 3px; }
  .title-line.second { margin-top: 14px; letter-spacing: 8px; }
  .ribbon { position: absolute; width: 114px; height: 102px; }
  .feature {
    position: absolute; width: 330px; color: var(--accent-orange);
    font-family: "Quicksand", sans-serif; font-weight: 700; font-size: 26px; line-height: 34px;
  }
  .feature.left { text-align: right; left: 10px; }
  .feature.right { text-align: left; left: 710px; }
</style>
</head>
<body>
<div class="canvas">
  <div class="postcard">
    <div class="network-backdrop" role="img" aria-label="Soft grey network of connected dots and lines"></div>

    <div class="brand">
      <div class="brand-mark"></div>
      <div class="brand-initials">HCP</div>
      <div class="brand-name">Harborline Capital Partners</div>
    </div>

    <div class="advisor-figure" role="img" aria-label="Blue silhouette of a business advisor with arms crossed"></div>

    <h1 class="title"><span class="title-line">STEADY</span><span class="title-line second">HARVEST</span></h1>

    <!-- Row 1 -->
    <p class="feature left" style="top:280px">Top Ranked<br>Strategy</p>
    <svg class="ribbon" style="left:374px;top:273px" viewBox="0 0 114 102">
      <polygon points="0,0 114,0 114,102 57,80 0,102" fill="var(--ribbon-blue)"/>
      <g stroke="var(--icon-white)" stroke-width="2.5" fill="none" stroke-linecap="round" stroke-linejoin="round">
        <path d="M38 22 V56 H78"/>
        <path d="M45 48 L53 38 L59 44 L72 28"/>
        <path d="M65 28 H72 V35"/>
      </g>
    </svg>

    <p class="feature right" style="top:284px">Minimums as low as<br>$50,000</p>
    <svg class="ribbon" style="left:581px;top:273px" viewBox="0 0 114 102">
      <polygon points="0,0 114,0 114,102 57,80 0,102" fill="var(--ribbon-pink)"/>
      <g fill="var(--icon-white)">
        <circle cx="40" cy="24" r="5"/>
        <rect x="34" y="31" width="12" height="20" rx="3"/>
        <circle cx="70" cy="28" r="8"/>
        <rect x="58" y="42" width="22" height="4" rx="2"/>
        <rect x="58" y="48" width="22" height="4" rx="2"/>
        <rect x="58" y="54" width="22" height="4" rx="2"/>
      </g>
      <text x="70" y="32" text-anchor="middle" font-family="Lato, sans-serif" font-weight="700" font-size="11" fill="var(--ribbon-pink)">$</text>
    </svg>

    <!-- Row 2 -->
    <p class="feature left" style="top:430px">Above Average<br>Income</p>
    <svg class="ribbon" style="left:374px;top:421px" viewBox="0 0 114 102">
      <polygon points="0,0 114,0 114,102 57,80 0,102" fill="var(--ribbon-wine)"/>
      <circle cx="57" cy="30" r="11" fill="none" stroke="var(--icon-white)" stroke-width="2.5"/>
      <text x="57" y="35" text-anchor="middle" font-family="Lato, sans-serif" font-weight="700" font-size="14" fill="var(--icon-white)">$</text>
      <rect x="38" y="48" width="38" height="10" rx="5" fill="var(--icon-white)"/>
    </svg>

    <p class="feature right" style="top:432px">Current Income<br>around 6% to 7%</p>
    <svg class="ribbon" style="left:581px;top:421px" viewBox="0 0 114 102">
      <polygon points="0,0 114,0 114,102 57,80 0,102" fill="var(--ribbon-lime)"/>
      <g fill="var(--icon-white)">
        <circle cx="57" cy="20" r="5"/>
        <rect x="51" y="27" width="12" height="22" rx="3"/>
        <ellipse cx="57" cy="56" rx="16" ry="4"/>
      </g>
      <g font-family="Lato, sans-serif" font-weight="700" font-size="11" fill="var(--icon-white)">
        <text x="36" y="28">%</text><text x="70" y="28">%</text>
      </g>
    </svg>

    <!-- Row 3 -->
    <p class="feature left" style="top:583px">Available in both<br>SMA and UMA</p>
    <svg class="ribbon" style="left:374px;top:571px" viewBox="0 0 114 102">
      <polygon points="0,0 114,0 114,102 57,80 0,102" fill="var(--ribbon-teal)"/>
      <g fill="none" stroke="var(--icon-white)" stroke-width="2.5">
        <circle cx="44" cy="24" r="8"/>
        <circle cx="72" cy="24" r="8"/>
        <circle cx="58" cy="48" r="8"/>
        <path d="M52 24 H64 M48 31 L54 41 M68 31 L62 41"/>
      </g>
    </svg>

    <p class="feature right" style="top:581px">Outpaced the Q&amp;R 700<br>since inception</p>
    <svg class="ribbon" style="left:581px;top:571px" viewBox="0 0 114 102">
      <polygon points="0,0 114,0 114,102 57,80 0,102" fill="var(--ribbon-grey)"/>
      <circle cx="57" cy="30" r="13" fill="var(--icon-white)"/>
      <polygon points="48,40 44,58 52,54 56,60 57,42" fill="var(--icon-white)"/>
      <polygon points="66,40 70,58 62,54 58,60 57,42" fill="var(--icon-white)"/>
    </svg>
  </div>
</div>
</body>
</html>
```